hotel amenities supply company needs design for bottles and accessories

we need to design four 30ml amenity tubes branded "VELORA" , shampoo, shower gel, conditioner and body lotion. the bottle has to be somewhat clear to be able to see the liquid inside. its basically designing the complete identity for "velora". attached are some examples. also the accessory boxes should match the design eg, shaving kit,vanity kit, toothbrush etc

Target Market(s)

hotels

Industry/Entity Type

Hotel

Font styles to use
Script

Requirements
Must have
• name "velora " on bottles and product info
Should not have
• dark colors

```html
<!DOCTYPE html>
<html lang="en">
<head>
<meta charset="utf-8">
<title>Velora Amenity Tubes</title>
<link rel="stylesheet" href="https://fonts.googleapis.com/css2?family=Rajdhani:wght@500&display=swap">
<style>
  :root {
    --page: #ffffff;
    --tube-edge: #e4e4e4;
    --crimp: #f7f7f7;
    --cap: #fbfbfb;
    --cap-shade: #ececec;
    --ink: #222222;
    --rule: #3a3a3a;
    --floral: rgba(150, 150, 150, 0.35);
    --shampoo-tint: #eef2d6;
    --conditioner-tint: #e5f0da;
    --gel-tint: #e5e3f3;
    --lotion-tint: #f3ebe9;
    --shampoo-accent: #a6c83a;
    --conditioner-accent: #6cb53a;
    --gel-accent: #a24aa6;
    --lotion-accent: #e58aa8;
  }
  * { margin: 0; padding: 0; box-sizing: border-box; }
  html, body { width: 1176px; height: 1200px; overflow: hidden; background: var(--page); }
  .canvas { position: relative; width: 1176px; height: 1200px; }
  .tube { position: absolute; top: 314px; width: 240px; height: 640px; }
  .tube-shape { position: absolute; inset: 0; }
  .product-label {
    position: absolute; left: 12px; top: 86px;
    padding: 0 0 6px 30px;
    border-bottom: 1.5px solid var(--rule);
    font-family: "Rajdhani", sans-serif; font-weight: 500;
    font-size: 23px; letter-spacing: 1px; color: var(--ink);
    white-space: nowrap;
  }
  .brand-name {
    position: absolute; left: 133px; top: 326px;
    transform: translate(-50%, -50%) rotate(90deg);
    font-family: "Rajdhani", sans-serif; font-weight: 500;
    font-size: 60px; letter-spacing: 4px; color: var(--ink);
    white-space: nowrap;
  }
  .brand-dot {
    position: absolute; left: 104px; top: 257px;
    width: 12px; height: 12px; border-radius: 50%;
  }
  .floral-area {
    position: absolute; left: 62px; top: 362px;
    width: 126px; height: 122px; border-radius: 40%;
    background: radial-gradient(circle at 50% 55%, var(--floral), rgba(150,150,150,0.08) 75%, transparent);
  }
  .shampoo { left: 58px; }
  .conditioner { left: 328px; }
  .shower-gel { left: 599px; }
  .body-lotion { left: 870px; }
  .shampoo .brand-dot { background: var(--shampoo-accent); }
  .conditioner .brand-dot { background: var(--conditioner-accent); }
  .shower-gel .brand-dot { background: var(--gel-accent); }
  .body-lotion .brand-dot { background: var(--lotion-accent); }
</style>
</head>
<body>
<main class="canvas">

  <section class="tube shampoo">
    <svg class="tube-shape" viewBox="0 0 240 640" width="240" height="640">
      <path d="M2 36 L238 36 L222 494 L18 494 Z" fill="var(--shampoo-tint)" stroke="var(--tube-edge)"/>
      <rect x="0" y="0" width="240" height="38" rx="4" fill="var(--crimp)" stroke="var(--tube-edge)"/>
      <path d="M34 494 L206 494 L200 636 Q120 642 40 636 Z" fill="var(--cap)" stroke="var(--tube-edge)"/>
      <rect x="96" y="566" width="48" height="40" rx="6" fill="none" stroke="var(--cap-shade)" stroke-width="3"/>
    </svg>
    <div class="product-label">SHAMPOO</div>
    <div class="brand-dot"></div>
    <div class="floral-area" role="img" aria-label="Soft grey floral decoration"></div>
    <div class="brand-name">Velora</div>
  </section>

  <section class="tube conditioner">
    <svg class="tube-shape" viewBox="0 0 240 640" width="240" height="640">
      <path d="M2 36 L238 36 L222 494 L18 494 Z" fill="var(--conditioner-tint)" stroke="var(--tube-edge)"/>
      <rect x="0" y="0" width="240" height="38" rx="4" fill="var(--crimp)" stroke="var(--tube-edge)"/>
      <path d="M34 494 L206 494 L200 636 Q120 642 40 636 Z" fill="var(--cap)" stroke="var(--tube-edge)"/>
      <rect x="96" y="566" width="48" height="40" rx="6" fill="none" stroke="var(--cap-shade)" stroke-width="3"/>
    </svg>
    <div class="product-label" style="padding-left:0;">HAIR CONDITIONER</div>
    <div class="brand-dot"></div>
    <div class="floral-area" role="img" aria-label="Soft grey floral decoration"></div>
    <div class="brand-name">Velora</div>
  </section>

  <section class="tube shower-gel">
    <svg class="tube-shape" viewBox="0 0 240 640" width="240" height="640">
      <path d="M2 36 L238 36 L222 494 L18 494 Z" fill="var(--gel-tint)" stroke="var(--tube-edge)"/>
      <rect x="0" y="0" width="240" height="38" rx="4" fill="var(--crimp)" stroke="var(--tube-edge)"/>
      <path d="M34 494 L206 494 L200 636 Q120 642 40 636 Z" fill="var(--cap)" stroke="var(--tube-edge)"/>
      <rect x="96" y="566" width="48" height="40" rx="6" fill="none" stroke="var(--cap-shade)" stroke-width="3"/>
    </svg>
    <div class="product-label">SHOWER GEL</div>
    <div class="brand-dot"></div>
    <div class="floral-area" role="img" aria-label="Soft grey floral decoration"></div>
    <div class="brand-name">Velora</div>
  </section>

  <section class="tube body-lotion">
    <svg class="tube-shape" viewBox="0 0 240 640" width="240" height="640">
      <path d="M2 36 L238 36 L222 494 L18 494 Z" fill="var(--lotion-tint)" stroke="var(--tube-edge)"/>
      <rect x="0" y="0" width="240" height="38" rx="4" fill="var(--crimp)" stroke="var(--tube-edge)"/>
      <path d="M34 494 L206 494 L200 636 Q120 642 40 636 Z" fill="var(--cap)" stroke="var(--tube-edge)"/>
      <rect x="96" y="566" width="48" height="40" rx="6" fill="none" stroke="var(--cap-shade)" stroke-width="3"/>
    </svg>
    <div class="product-label">BODY LOTION</div>
    <div class="brand-dot"></div>
    <div class="floral-area" role="img" aria-label="Soft grey floral decoration"></div>
    <div class="brand-name">Velora</div>
  </section>

</main>
</body>
</html>
```